custom carpentry, woodworking and home repair company needs logo design and business card design

Attention: I apologize but I just received notification from my state that I cannot use the company name that I originally submitted (Beyond The Bench). The new name will be Lumbrella We need a company logo and business card design for our new company based in the Hampton Roads area of Virginia. The company name is Lumbrella. The final design should give a first impression of true craftsmanship and attention to detail. We would like the card to include the company name, my name Derek Halloway (owner), phone number (757) 482-3175, website (lumbrella-shop.example) and email address (derek@lumbrella-shop.example). Everything else is up to your discretion. Thanks, have fun, and good luck.

Industry/Entity Type

Business

Contact Information for Business Card

See project description

Logo Text

see project description

Colors

Designer to choose colors to be used in the design.

```html
<!DOCTYPE html>
<html lang="en">
<head>
<meta charset="utf-8">
<title>Lumbrella Business Card</title>
<link rel="stylesheet" href="https://fonts.googleapis.com/css2?family=Roboto:wght@400;500;700&display=swap">
<style>
  :root {
    --backdrop: #d9d9d7;
    --card-paper: #f4f2ed;
    --ink-brown: #6a3b1f;
    --ink-brown-soft: #7d4a2a;
    --wood-dark: #3b2117;
    --wood-mid: #5a3322;
    --wood-light: #6e4230;
    --on-wood: #ffffff;
  }
  * { margin: 0; padding: 0; box-sizing: border-box; }
  html, body {
    width: 1200px; height: 900px; overflow: hidden;
    background: var(--backdrop);
    font-family: "Roboto", Arial, sans-serif;
  }
  .canvas {
    position: relative; width: 1200px; height: 900px;
    display: flex; justify-content: center; align-items: center; gap: 70px;
  }
  .card {
    width: 340px; height: 595px; border-radius: 28px;
    position: relative; overflow: hidden;
    box-shadow: 0 10px 28px rgba(0,0,0,0.18);
  }
  .card-front {
    background: var(--card-paper);
    color: var(--ink-brown);
    text-align: center;
    display: flex; flex-direction: column; align-items: center;
    padding-top: 46px;
  }
  .holder-name { font-size: 22px; font-weight: 700; letter-spacing: 0.5px; }
  .holder-role { font-size: 15px; font-weight: 500; color: var(--ink-brown-soft); margin-top: 2px; }
  .brand { display: flex; flex-direction: column; align-items: center; margin-top: 28px; }
  .brand-square { width: 176px; height: 142px; border: 2px solid var(--ink-brown); }
  .brand-name { font-size: 36px; font-weight: 500; margin-top: 18px; letter-spacing: 0.5px; }
  .address { font-size: 15px; font-weight: 500; line-height: 1.3; margin-top: 34px; color: var(--ink-brown-soft); }
  .contact-icons { display: flex; gap: 22px; margin-top: 26px; }
  .contact-icon {
    width: 30px; height: 30px; border-radius: 50%;
    background: var(--ink-brown);
    display: flex; align-items: center; justify-content: center;
  }
  .contact-lines { margin-top: 26px; font-size: 16px; line-height: 1.6; color: var(--ink-brown-soft); font-weight: 500; }
  .contact-lines .phone { font-size: 18px; font-weight: 400; }
  .contact-lines strong { font-weight: 700; }

  .card-back { background: var(--wood-mid); }
  .wood-surface {
    position: absolute; inset: 0;
    background:
      linear-gradient(90deg,
        var(--wood-dark) 0%, var(--wood-mid) 8%, var(--wood-light) 16%,
        var(--wood-mid) 26%, var(--wood-dark) 34%, var(--wood-mid) 46%,
        var(--wood-light) 58%, var(--wood-mid) 70%, var(--wood-dark) 82%,
        var(--wood-mid) 92%, var(--wood-dark) 100%);
  }
  .back-brand {
    position: absolute; left: 0; right: 0; top: 170px;
    display: flex; flex-direction: column; align-items: center;
    color: var(--on-wood);
  }
  .back-brand .brand-square { border-color: var(--on-wood); width: 196px; height: 158px; }
  .back-brand .brand-name { font-size: 40px; }
</style>
</head>
<body>
<main class="canvas">
  <article class="card card-front">
    <h1 class="holder-name">DEREK HALLOWAY</h1>
    <p class="holder-role">Managing Director</p>

    <div class="brand">
      <div class="brand-square"></div>
      <p class="brand-name">Lumbrella</p>
    </div>

    <p class="address">48 Harbor Mill Lane, Tidewater Park,<br>Virginia United States</p>

    <div class="contact-icons">
      <span class="contact-icon" aria-label="Phone">
        <svg width="16" height="16" viewBox="0 0 24 24"><path fill="#f4f2ed" d="M6.6 10.8a15 15 0 0 0 6.6 6.6l2.2-2.2a1 1 0 0 1 1-.25 11.4 11.4 0 0 0 3.6.57 1 1 0 0 1 1 1V20a1 1 0 0 1-1 1A17 17 0 0 1 3 4a1 1 0 0 1 1-1h3.5a1 1 0 0 1 1 1c0 1.25.2 2.45.57 3.57a1 1 0 0 1-.25 1z"/></svg>
      </span>
      <span class="contact-icon" aria-label="Email">
        <svg width="16" height="16" viewBox="0 0 24 24"><rect x="3" y="6" width="18" height="12" rx="1" fill="none" stroke="#f4f2ed" stroke-width="2"/><path d="M3 7l9 6 9-6" fill="none" stroke="#f4f2ed" stroke-width="2"/></svg>
      </span>
      <span class="contact-icon" aria-label="Website">
        <svg width="16" height="16" viewBox="0 0 24 24"><path d="M10 14a4 4 0 0 0 5.6 0l3-3a4 4 0 0 0-5.6-5.6l-1 1M14 10a4 4 0 0 0-5.6 0l-3 3a4 4 0 0 0 5.6 5.6l1-1" fill="none" stroke="#f4f2ed" stroke-width="2.2" stroke-linecap="round"/></svg>
      </span>
    </div>

    <div class="contact-lines">
      <p class="phone">(757) 482-3175</p>
      <p>derek@lumbrella-shop.example</p>
      <p>www.<strong>lumbrella-shop</strong>.example</p>
    </div>
  </article>

  <article class="card card-back">
    <div class="wood-surface" role="img" aria-label="Dark walnut wood grain surface"></div>
    <div class="back-brand">
      <div class="brand-square"></div>
      <p class="brand-name">Lumbrella</p>
    </div>
  </article>
</main>
</body>
</html>
```